Roofing & Siding door hanger flyer

-Looking to make door hanger flyer for Korvell Roofing & Siding
-4.5" wide x 11" tall
-2 sided full colour
-We have started a new website (the content is changing) I have attached photos.
-About us:
-25 year labour warranty's available
-32 years in Calgary
-QHT A+ Member
-NWPC (Prairie Westmark Shingle Council) (logo attached)
-TEK Summit Premier (logo attached)
-Owen Calloway (logo attached)
-Slogan "Raised On Grit, Proven Through Storms" 32 years in Calgary
-Sale
-Page 1 & 2 design ideas
We are in your area, contact us today for your Exclusive limited time offer! *discounts apply exclusively to new agreements only
Updates
-Please keep simple, clean & bright
-I really like the bright blue from our new logo (new logo uploaded)
-We specialize in Roofing -Siding-Gutters & full Exterior Renos (like the competitor example uploaded)
-This is the NEW website we are currently working on (not finished) https://mockups.plenvio.net/view/8b2c4e71-d95a-4f0b-b7e3-c1c1c8823a7f-9d2b/?fullscreen
-This is our OLD website https://northpeakshinglepros.com
-For the sale "We are in your area, contact us today for your Exclusive limited time offer" *discounts apply exclusively to new agreements only
-Free Estimates
-our phone# is 403-555-0187
-our website is northpeakshinglepros.com
-keep simple, clean, bright use the "new logo" uploaded. Check out the competitor example uploaded file
-We are in your area, Contact us today for your Exclusive limited time offer! *discounts apply to new agreements only
-FREE ESTIMATES
-Specialized in Roofing /Siding /Gutters Full Exterior Reno's
-We are currently working on a NEW website https://mockups.plenvio.net/view/8b2c4e71-d95a-4f0b-b7e3-c1c1c8823a7f-9d2b/?fullscreen
-Our OLD website https://northpeakshinglepros.com/
-Post old site address on flyer northpeakshinglepros.com
-Phone # 403-555-0187
Target Market(s)
40-55
Industry/Entity Type
Roofing Siding & full Exterior Reno's
Look and feel

```html
<!DOCTYPE html>
<html lang="en">
<head>
<meta charset="utf-8">
<title>Korvell Roofing &amp; Siding – Door Hanger</title>
<link href="https://fonts.googleapis.com/css2?family=Poppins:wght@400;500;600;700;800&display=swap" rel="stylesheet">
<style>
:root{
  --page-blue:#3b8fd4;
  --brand-blue:#1c63b5;
  --navy:#1a4d8c;
  --red:#e8202a;
  --ink:#222428;
  --white:#ffffff;
  --soft-grey:#e6e8ec;
}
*{margin:0;padding:0;box-sizing:border-box}
html,body{width:1056px;height:1200px;overflow:hidden}
body{background:var(--page-blue);font-family:'Poppins',sans-serif;position:relative}
.hanger{position:absolute;top:148px;width:355px;height:868px;background:var(--white);overflow:hidden;box-shadow:0 6px 18px rgba(0,0,0,.18)}
.hanger--front{left:150px}
.hanger--back{left:551px}
.hanger-shapes{position:absolute;inset:0}
.hanger-hole{position:absolute;left:138px;top:61px;width:80px;height:80px;border-radius:50%;background:var(--page-blue);z-index:5}
.abs{position:absolute}
.top-callout{left:0;width:355px;top:26px;text-align:center;color:var(--white);font-weight:600;font-size:16px;line-height:15px;z-index:3}
.headline{left:0;width:355px;text-align:center;color:var(--white);font-weight:800;z-index:3}
.headline--front{top:148px;font-size:21px;line-height:23px}
.headline--back{top:146px;font-size:24px;line-height:26px}
.photo{position:absolute}
.brand{display:flex;align-items:center;gap:8px;color:var(--ink);font-weight:500;z-index:3}
.brand-mark{width:14px;height:14px;background:var(--brand-blue)}
.brand-name{font-size:25px;line-height:26px;letter-spacing:2px}
.brand-sub{font-size:10.5px;letter-spacing:3px;line-height:14px}
.label-bar{background:var(--brand-blue);color:var(--white);font-weight:800;font-size:16px;line-height:20px;height:20px;padding:0 10px;z-index:3;transform:skewX(-12deg)}
.label-bar span{display:inline-block;transform:skewX(12deg)}
.label-bar em{font-style:normal;font-weight:400}
.check-list{list-style:none;z-index:3;color:var(--ink)}
.check-list li{display:flex;align-items:center;gap:4px}
.check-list svg{flex:none}
.list-lg{font-size:11.5px;line-height:21px}
.list-sm{font-size:10px;line-height:11px}
.list-sm li{border-bottom:1px solid var(--soft-grey);padding:3px 0 4px;width:78px;align-items:flex-start}
.list-sm--right li{width:88px;white-space:nowrap}
.badge{width:75px;height:31px;background:var(--white);box-shadow:0 1px 4px rgba(0,0,0,.25);display:flex;align-items:center;justify-content:center}
.badge-shape{width:32px;height:18px;background:var(--brand-blue);border-radius:3px}
.badge-shape--round{width:20px;height:20px;border-radius:50%;background:#2f9e58}
.badge-shape--diamond{width:18px;height:18px;transform:rotate(45deg);background:#1d3f7a;border-radius:2px}
.badge-shape--red{background:var(--red);width:40px;height:12px}
.sale{color:var(--brand-blue);font-size:7.5px;line-height:7.5px;font-weight:500;width:108px;z-index:3}
.sale small{display:block;color:var(--ink);font-size:5.5px;line-height:6px;margin-top:3px;font-weight:400}
.footer-phone{top:843px;left:46px;color:var(--white);font-weight:700;font-size:14px;display:flex;align-items:center;gap:3px;z-index:3}
.footer-web{top:848px;left:189px;color:var(--white);font-weight:600;font-size:7px;display:flex;align-items:center;gap:3px;z-index:3}
.about-title{color:var(--white)}
.about-copy{left:172px;top:385px;width:142px;font-size:8.3px;line-height:10px;color:#4a4d55;z-index:3}
.about-copy p+p{margin-top:8px}
.promise{left:53px;width:251px;height:29px;color:var(--white);font-weight:700;font-size:11.5px;text-align:center;line-height:29px;transform:skewX(-14deg);z-index:3}
.promise span{display:inline-block;transform:skewX(14deg)}
.promise--blue{background:var(--brand-blue)}
.promise--red{background:var(--red)}
</style>
</head>
<body>

<section class="hanger hanger--front">
  <svg class="hanger-shapes" width="355" height="868" viewBox="0 0 355 868" aria-hidden="true">
    <defs>
      <linearGradient id="heroFront" x1="0" y1="0" x2="1" y2="1">
        <stop offset="0" stop-color="#1f5596"/><stop offset="1" stop-color="#163f78"/>
      </linearGradient>
    </defs>
    <rect x="0" y="60" width="355" height="250" fill="url(#heroFront)"/>
    <polygon points="0,0 355,0 355,62 0,92" fill="var(--red)"/>
    <polygon points="170,88 355,60 355,88" fill="var(--brand-blue)"/>
    <polygon points="190,278 355,254 355,276" fill="var(--red)"/>
    <polygon points="0,292 355,270 355,868 0,868" fill="var(--white)"/>
    <polygon points="225,830 355,810 355,826" fill="var(--brand-blue)"/>
    <polygon points="0,836 355,822 355,868 0,868" fill="var(--red)"/>
  </svg>
  <div class="hanger-hole"></div>
  <div class="abs top-callout">WE’RE IN<br>YOUR NEIGHBOURHOOD!</div>
  <h1 class="abs headline headline--front">We Specialize In<br>Roofing -siding-gutters<br>&amp; Full Exterior Renos</h1>

  <div class="photo" role="img" aria-label="Close-up of a grey shingle roof" style="left:0;top:292px;width:150px;height:186px;background:linear-gradient(135deg,#8a8c90,#55585e)"></div>
  <div class="photo" role="img" aria-label="Brick house with snow on the roof" style="left:205px;top:470px;width:150px;height:132px;background:linear-gradient(160deg,#c9cdd4,#8a6f58)"></div>
  <div class="photo" role="img" aria-label="Two-storey home with double garage" style="left:0;top:612px;width:155px;height:150px;background:linear-gradient(170deg,#a9c7e8,#c9b9a4 60%,#6f9a55)"></div>

  <div class="abs brand" style="left:190px;top:300px;flex-direction:column;align-items:flex-start;gap:0">
    <div style="display:flex;align-items:center;gap:8px"><span class="brand-mark"></span><span class="brand-name">KORVELL</span></div>
    <span class="brand-sub">ROOFING &amp; SIDING</span>
  </div>

  <div class="abs label-bar" style="left:150px;top:377px;width:195px"><span>Roofing <em>*centred*</em></span></div>
  <ul class="abs check-list list-lg" style="left:169px;top:400px">
    <li><svg width="7" height="7" viewBox="0 0 10 10"><circle cx="5" cy="5" r="4.3" fill="none" stroke="#e8202a" stroke-width="1.4"/><path d="M3 5.2l1.5 1.5L7.2 3.6" fill="none" stroke="#e8202a" stroke-width="1.4"/></svg>Asphalt</li>
    <li><svg width="7" height="7" viewBox="0 0 10 10"><circle cx="5" cy="5" r="4.3" fill="none" stroke="#e8202a" stroke-width="1.4"/><path d="M3 5.2l1.5 1.5L7.2 3.6" fill="none" stroke="#e8202a" stroke-width="1.4"/></svg>Rubber</li>
    <li><svg width="7" height="7" viewBox="0 0 10 10"><circle cx="5" cy="5" r="4.3" fill="none" stroke="#e8202a" stroke-width="1.4"/><path d="M3 5.2l1.5 1.5L7.2 3.6" fill="none" stroke="#e8202a" stroke-width="1.4"/></svg>Metal</li>
  </ul>

  <div class="abs label-bar" style="left:-6px;top:486px;width:200px;padding-left:48px"><span>Siding<em>*centred*</em></span></div>
  <ul class="abs check-list list-lg" style="left:42px;top:509px">
    <li><svg width="7" height="7" viewBox="0 0 10 10"><circle cx="5" cy="5" r="4.3" fill="none" stroke="#e8202a" stroke-width="1.4"/><path d="M3 5.2l1.5 1.5L7.2 3.6" fill="none" stroke="#e8202a" stroke-width="1.4"/></svg>Calloway fibre cement</li>
    <li><svg width="7" height="7" viewBox="0 0 10 10"><circle cx="5" cy="5" r="4.3" fill="none" stroke="#e8202a" stroke-width="1.4"/><path d="M3 5.2l1.5 1.5L7.2 3.6" fill="none" stroke="#e8202a" stroke-width="1.4"/></svg>Vinyl</li>
    <li><svg width="7" height="7" viewBox="0 0 10 10"><circle cx="5" cy="5" r="4.3" fill="none" stroke="#e8202a" stroke-width="1.4"/><path d="M3 5.2l1.5 1.5L7.2 3.6" fill="none" stroke="#e8202a" stroke-width="1.4"/></svg>Metal (Steel, Aluminum)</li>
    <li><svg width="7" height="7" viewBox="0 0 10 10"><circle cx="5" cy="5" r="4.3" fill="none" stroke="#e8202a" stroke-width="1.4"/><path d="M3 5.2l1.5 1.5L7.2 3.6" fill="none" stroke="#e8202a" stroke-width="1.4"/></svg>longboard</li>
  </ul>

  <div class="abs label-bar" style="left:84px;top:620px;width:260px;text-align:right"><span>Full Exteriors <em>*centred*</em></span></div>
  <ul class="abs check-list list-sm" style="left:165px;top:646px">
    <li><svg width="7" height="7" viewBox="0 0 10 10"><circle cx="5" cy="5" r="4.3" fill="none" stroke="#e8202a" stroke-width="1.4"/><path d="M3 5.2l1.5 1.5L7.2 3.6" fill="none" stroke="#e8202a" stroke-width="1.4"/></svg><span>Eavestrough/soffit /fascia</span></li>
    <li><svg width="7" height="7" viewBox="0 0 10 10"><circle cx="5" cy="5" r="4.3" fill="none" stroke="#e8202a" stroke-width="1.4"/><path d="M3 5.2l1.5 1.5L7.2 3.6" fill="none" stroke="#e8202a" stroke-width="1.4"/></svg>Stone</li>
    <li><svg width="7" height="7" viewBox="0 0 10 10"><circle cx="5" cy="5" r="4.3" fill="none" stroke="#e8202a" stroke-width="1.4"/><path d="M3 5.2l1.5 1.5L7.2 3.6" fill="none" stroke="#e8202a" stroke-width="1.4"/></svg>Skylight</li>
    <li><svg width="7" height="7" viewBox="0 0 10 10"><circle cx="5" cy="5" r="4.3" fill="none" stroke="#e8202a" stroke-width="1.4"/><path d="M3 5.2l1.5 1.5L7.2 3.6" fill="none" stroke="#e8202a" stroke-width="1.4"/></svg><span>Windows &amp; Doors</span></li>
  </ul>
  <ul class="abs check-list list-sm list-sm--right" style="left:250px;top:669px">
    <li><svg width="7" height="7" viewBox="0 0 10 10"><circle cx="5" cy="5" r="4.3" fill="none" stroke="#e8202a" stroke-width="1.4"/><path d="M3 5.2l1.5 1.5L7.2 3.6" fill="none" stroke="#e8202a" stroke-width="1.4"/></svg>stucco</li>
    <li><svg width="7" height="7" viewBox="0 0 10 10"><circle cx="5" cy="5" r="4.3" fill="none" stroke="#e8202a" stroke-width="1.4"/><path d="M3 5.2l1.5 1.5L7.2 3.6" fill="none" stroke="#e8202a" stroke-width="1.4"/></svg>Insulation</li>
    <li><svg width="7" height="7" viewBox="0 0 10 10"><circle cx="5" cy="5" r="4.3" fill="none" stroke="#e8202a" stroke-width="1.4"/><path d="M3 5.2l1.5 1.5L7.2 3.6" fill="none" stroke="#e8202a" stroke-width="1.4"/></svg>Painting</li>
    <li><svg width="7" height="7" viewBox="0 0 10 10"><circle cx="5" cy="5" r="4.3" fill="none" stroke="#e8202a" stroke-width="1.4"/><path d="M3 5.2l1.5 1.5L7.2 3.6" fill="none" stroke="#e8202a" stroke-width="1.4"/></svg>Shake Repairs</li>
  </ul>

  <div class="abs badge" style="left:165px;top:757px"><span class="badge-shape badge-shape--red"></span></div>
  <div class="abs badge" style="left:246px;top:757px"><span class="badge-shape"></span></div>
  <div class="abs badge" style="left:165px;top:792px"><span class="badge-shape badge-shape--diamond"></span></div>
  <div class="abs badge" style="left:246px;top:792px"><span class="badge-shape badge-shape--round"></span></div>

  <p class="abs sale" style="left:42px;top:790px">We are in your area, contact us today for your Exclusive limited time offer*<small>*discounts apply exclusively to new agreements only</small></p>

  <div class="abs footer-phone"><svg width="10" height="10" viewBox="0 0 24 24"><path d="M6.6 10.8a15 15 0 006.6 6.6l2.2-2.2a1 1 0 011-.25 11.4 11.4 0 003.6.57 1 1 0 011 1V20a1 1 0 01-1 1A17 17 0 013 4a1 1 0 011-1h3.5a1 1 0 011 1 11.4 11.4 0 00.57 3.6 1 1 0 01-.25 1z" fill="#fff"/></svg>403-555-0187</div>
  <div class="abs footer-web"><svg width="8" height="8" viewBox="0 0 24 24"><circle cx="12" cy="12" r="10" fill="none" stroke="#fff" stroke-width="2"/><path d="M2 12h20M12 2c3 3 3 17 0 20M12 2c-3 3-3 17 0 20" fill="none" stroke="#fff" stroke-width="2"/></svg>www.northpeakshinglepros.com</div>
</section>

<section class="hanger hanger--back">
  <svg class="hanger-shapes" width="355" height="868" viewBox="0 0 355 868" aria-hidden="true">
    <defs>
      <linearGradient id="heroBack" x1="0" y1="0" x2="1" y2="1">
        <stop offset="0" stop-color="#2a63a8"/><stop offset="1" stop-color="#163f78"/>
      </linearGradient>
    </defs>
    <rect x="0" y="60" width="355" height="250" fill="url(#heroBack)"/>
    <polygon points="0,0 355,0 355,62 0,92" fill="var(--red)"/>
    <polygon points="170,88 355,60 355,88" fill="var(--brand-blue)"/>
    <polygon points="190,278 355,254 355,276" fill="var(--red)"/>
    <polygon points="0,292 355,270 355,868 0,868" fill="var(--white)"/>
    <polygon points="225,830 355,810 355,826" fill="var(--brand-blue)"/>
    <polygon points="0,836 355,822 355,868 0,868" fill="var(--red)"/>
  </svg>
  <div class="hanger-hole"></div>
  <div class="abs top-callout">WE’RE IN<br>YOUR NEIGHBOURHOOD!</div>
  <h1 class="abs headline headline--back">Raised On Grit,<br>Proven Through<br>Storms</h1>

  <div class="photo" role="img" aria-label="Grey two-storey house with lit garage at dusk" style="left:0;top:292px;width:150px;height:196px;background:linear-gradient(170deg,#b8c6d8,#6c7b8e 55%,#5b8a44)"></div>
  <div class="photo" role="img" aria-label="Cedar shake siding detail" style="left:0;top:620px;width:190px;height:122px;background:linear-gradient(150deg,#c79a6a,#8e6240);clip-path:polygon(0 0,100% 0,82% 100%,0 100%)"></div>
  <div class="photo" role="img" aria-label="Brown-roofed house with white porch" style="left:172px;top:620px;width:183px;height:122px;background:linear-gradient(170deg,#9fc1e3,#8b6c55 55%,#4f7a3c);clip-path:polygon(10% 0,100% 0,100% 100%,0 100%)"></div>

  <div class="abs brand" style="left:168px;top:292px;flex-direction:column;align-items:flex-start;gap:0">
    <div style="display:flex;align-items:center;gap:8px"><span class="brand-mark"></span><span class="brand-name">KORVELL</span></div>
    <span class="brand-sub">ROOFING &amp; SIDING</span>
  </div>

  <div class="abs label-bar about-title" style="left:158px;top:361px;width:160px"><span>About Us</span></div>
  <div class="abs about-copy">
    <p>Korvell Roofing &amp; Siding Ltd. has been focusing on you, the customer, since 1991.</p>
    <p>We pride ourselves in providing excellent customer service and quality workmanship. We work with honesty and integrity and staff expert managers, supervisors and tradespeople.</p>
  </div>

  <div class="abs promise promise--blue" style="top:500px"><span>25 year labour warranty's available</span></div>
  <div class="abs promise promise--red" style="top:538px"><span>32 years in Calgary</span></div>
  <div class="abs promise promise--blue" style="top:576px"><span>Free Estimates</span></div>

  <div class="abs badge" style="left:155px;top:757px"><span class="badge-shape badge-shape--red"></span></div>
  <div class="abs badge" style="left:236px;top:757px"><span class="badge-shape"></span></div>
  <div class="abs badge" style="left:155px;top:792px"><span class="badge-shape badge-shape--diamond"></span></div>
  <div class="abs badge" style="left:236px;top:792px"><span class="badge-shape badge-shape--round"></span></div>

  <p class="abs sale" style="left:42px;top:774px">We are in your area, contact us today for your Exclusive limited time offer*<small>*discounts apply exclusively to new agreements only</small></p>

  <div class="abs footer-phone"><svg width="10" height="10" viewBox="0 0 24 24"><path d="M6.6 10.8a15 15 0 006.6 6.6l2.2-2.2a1 1 0 011-.25 11.4 11.4 0 003.6.57 1 1 0 011 1V20a1 1 0 01-1 1A17 17 0 013 4a1 1 0 011-1h3.5a1 1 0 011 1 11.4 11.4 0 00.57 3.6 1 1 0 01-.25 1z" fill="#fff"/></svg>403-555-0187</div>
  <div class="abs footer-web"><svg width="8" height="8" viewBox="0 0 24 24"><circle cx="12" cy="12" r="10" fill="none" stroke="#fff" stroke-width="2"/><path d="M2 12h20M12 2c3 3 3 17 0 20M12 2c-3 3-3 17 0 20" fill="none" stroke="#fff" stroke-width="2"/></svg>www.northpeakshinglepros.com</div>
</section>

</body>
</html>
```